" A Limpinho Já é especializada em higienização e impermeabilização de estofados, tanto residenciais quanto automotivos. Também oferecemos serviços de lavanderia para itens como cortinas, edredons, toalhas e peças delicadas. Atendemos com praticidade e comodidade, oferecendo serviço a domicílio e sistema de delivery, sempre priorizando qualidade, cuidado e eficiência em cada atendimento. "

```html
<!DOCTYPE html>
<html lang="pt-BR">
<head>
<meta charset="UTF-8">
<title>Limpinho Já – Cartão de Visita</title>
<link href="https://fonts.googleapis.com/css2?family=Montserrat:wght@500;600;800&display=swap" rel="stylesheet">
<style>
  :root {
    --bg: #5a5a5c;
    --blue: #1c5aa6;
    --blue-dark: #164a8c;
    --blue-light: #3f8fe0;
    --white: #ffffff;
    --ink: #2a4e86;
    --text: #3a3a3a;
  }
  * { box-sizing: border-box; margin: 0; padding: 0; }
  html, body { width: 1200px; height: 1200px; overflow: hidden; }
  body {
    background: var(--bg);
    font-family: "Montserrat", sans-serif;
    display: flex; flex-direction: column; align-items: center; justify-content: center;
    gap: 80px;
  }
  .card {
    position: relative; width: 860px; height: 490px; overflow: hidden;
    border-radius: 6px;
  }
  .card--front {
    background: linear-gradient(135deg, var(--blue-light) -40%, var(--blue) 45%, var(--blue-dark) 100%);
  }
  .front-decor {
    position: absolute; left: -60px; bottom: -90px; width: 360px; height: 360px;
    border-radius: 50%; background: rgba(255,255,255,0.06);
  }
  .brand {
    display: flex; align-items: center; gap: 18px;
    font-weight: 800; letter-spacing: -1px;
  }
  .brand-dot { border-radius: 50%; flex: none; }
  .card--front .brand {
    position: absolute; left: 50%; top: 50%; transform: translate(-50%, -50%);
    color: var(--white); font-size: 86px;
  }
  .card--front .brand-dot { width: 60px; height: 60px; background: var(--white); }

  .card--back { background: var(--white); }
  .back-band { position: absolute; inset: 0; width: 100%; height: 100%; }
  .holder {
    position: absolute; left: 70px; top: 70px;
    color: var(--ink); font-weight: 600; font-size: 32px;
  }
  .card--back .brand {
    position: absolute; left: 70px; top: 250px;
    color: var(--blue); font-size: 46px; gap: 12px;
  }
  .card--back .brand-dot { width: 34px; height: 34px; background: var(--blue); }
  .contacts {
    position: absolute; left: 430px; top: 160px; list-style: none;
    display: flex; flex-direction: column; gap: 14px;
    color: var(--text); font-weight: 500; font-size: 19px; line-height: 1.25;
  }
  .contacts li { display: flex; align-items: center; gap: 14px; }
  .icon {
    width: 34px; height: 34px; border-radius: 50%; background: var(--blue);
    display: flex; align-items: center; justify-content: center; flex: none;
  }
  .icon svg { width: 18px; height: 18px; }
</style>
</head>
<body>
  <section class="card card--front" aria-label="Frente do cartão">
    <div class="front-decor"></div>
    <div class="brand"><span class="brand-dot"></span>Limpinho Já</div>
  </section>

  <section class="card card--back" aria-label="Verso do cartão">
    <svg class="back-band" viewBox="0 0 860 490" preserveAspectRatio="none" aria-hidden="true">
      <path d="M560 490 C 680 470 760 430 860 360 L860 490 Z" fill="#3f8fe0"/>
      <path d="M620 490 C 720 475 790 445 860 400 L860 490 Z" fill="#1c5aa6"/>
      <path d="M0 430 C 60 455 120 470 200 490 L0 490 Z" fill="#1c5aa6"/>
    </svg>
    <p class="holder">Nome e Sobrenome - Diretor Comercial</p>
    <div class="brand"><span class="brand-dot"></span>Limpinho Já</div>
    <ul class="contacts">
      <li><span class="icon"><svg viewBox="0 0 24 24"><path fill="#fff" d="M6.6 10.8a15 15 0 0 0 6.6 6.6l2.2-2.2a1 1 0 0 1 1-.25 11.4 11.4 0 0 0 3.6.57 1 1 0 0 1 1 1V20a1 1 0 0 1-1 1A17 17 0 0 1 3 4a1 1 0 0 1 1-1h3.5a1 1 0 0 1 1 1c0 1.25.2 2.45.57 3.57a1 1 0 0 1-.25 1z"/></svg></span>(71) 90000-1111 | (71) 90000-2222</li>
      <li><span class="icon"><svg viewBox="0 0 24 24"><path fill="#fff" d="M3 5h18v14H3z M3 5l9 7 9-7" stroke="#1c5aa6" stroke-width="1.6"/></svg></span>limpinhoja@email.com</li>
      <li><span class="icon"><svg viewBox="0 0 24 24"><path fill="#fff" d="M12 2a7 7 0 0 0-7 7c0 5 7 13 7 13s7-8 7-13a7 7 0 0 0-7-7zm0 9.5A2.5 2.5 0 1 1 12 6.5a2.5 2.5 0 0 1 0 5z"/></svg></span><span>Rua das Flores, 250<br>Cidade/UF - CEP: 40000-000</span></li>
      <li><span class="icon"><svg viewBox="0 0 24 24"><circle cx="12" cy="12" r="6" fill="#fff"/></svg></span>@limpinhoja</li>
    </ul>
  </section>
</body>
</html>
```